TALVEXO needs a Sleek, Professional and Serious Web Design, this web design is aiming to be famous!

Dear Designers,

We need a web design for a new company based on the Internet named "talvexo". I have already worked with PQ to get my logo and it has been a wonderful experience which I want to repeat. We are kind of work social network, the web page will be mostly used to write comments on businesses around the world to help workers find which company fit the best for them. This website is also here to help people finding work by giving them the tools to make the right research.

For contents inspiration, you could see on the added files a sketch of the website but I am not asking you following it because it was just for giving the contents.

We do not have any example regarding website that we do like because all are coming so generic. We would like a very sleek website, where surfing become very intuitive and ergonomic (Glimmerly is not very ergonomic for example from our point of view). The website must reflect professionalism and seriousness and worker, world connexion.

We will be pleased to accept original designs as long as they fit to our requirements and if it is properly made of course: e.g. web page looking like a newspaper etc.

About colours, we are not decided yet but we are aiming a light orange (pastel style) or dark bluish green. Also, it comes to our attention that a web site mostly realized in grey-scale will be very interesting (touch of colour will be accepted as well if it miss too much dynamism) .

We will give the feedback as soon as possible because we would like to have 5 pages but it will be only very small changes on the next ones. (like adding 4 buttons)

Target Market(s)

Our target is relatively large because it is all people of working age, in numbers we can say a range of people aged from 18 to 45 years.

Industry/Entity Type

Internet

Number of Pages Required

3 page

Font styles to use
Sans Serif

Requirements
Must have
• Elements that must be on the web page are exposed below:
• - company logo ( .ai & .eps files on added files)
• - 4 buttons (Searcher "highlighted" / Advises / Jobs / Solutions)
• - login/account window
• - language button (e.g. a flag)
• - Window companies searcher (the most important, refer to the sketch)
• - classic menu down the page - about us / contact us / conditions / site map / community / politics / publicity / languages / copyright etc.
Nice to have
• We want a professional and serious website.
Should not have
• If you have a doubt, just ask us because nothing are coming to our mind.

```html
<!DOCTYPE html>
<html lang="en">
<head>
<meta charset="utf-8">
<title>TALVEXO – Companies Searcher</title>
<link href="https://fonts.googleapis.com/css2?family=Source+Sans+3:wght@300;400;600;700;900&display=swap" rel="stylesheet">
<style>
  :root{
    --orange:#f8a41e;
    --ink:#2b2b2b;
    --logo:#3b3b3d;
    --blue-light:#0b7fd0;
    --blue-dark:#05569c;
    --footer:#3a3a3c;
    --footer-text:#e6e6e6;
    --field-border:#cfcfcf;
    --placeholder:#8a8a8a;
    --card-head:#f6f6f6;
    --white:#ffffff;
  }
  *{box-sizing:border-box;margin:0;padding:0}
  html,body{width:1200px;height:705px;overflow:hidden;background:var(--white)}
  body{font-family:"Source Sans 3",Arial,sans-serif;color:var(--ink);position:relative}

  .site-header{position:absolute;top:0;left:0;width:1200px;height:79px;background:var(--white)}
  .brand{position:absolute;left:120px;top:14px;display:flex;align-items:center;gap:10px}
  .brand-dot{width:26px;height:26px;border-radius:50%;background:var(--logo)}
  .brand-name{font-size:38px;font-weight:900;color:var(--logo);letter-spacing:.5px;line-height:48px}

  .main-nav{position:absolute;left:0;top:0;width:800px;height:79px;font-size:13px;font-weight:600;color:var(--ink)}
  .main-nav span{position:absolute;top:33px;white-space:nowrap;line-height:18px}
  .main-nav .is-active{color:var(--orange)}

  .language-select{position:absolute;left:813px;top:23px;width:129px;height:37px;border:1px solid #c9c9c9;border-radius:2px;font-size:12.5px;padding:0 10px;display:flex;align-items:center;justify-content:space-between;color:var(--ink)}
  .login-button{position:absolute;left:949px;top:22px;width:131px;height:39px;background:var(--orange);border-radius:3px;color:var(--white);font-size:12.5px;display:flex;align-items:center;justify-content:center}

  .hero{position:absolute;top:79px;left:0;width:1200px;height:512px;background:radial-gradient(ellipse at 50% 40%,var(--blue-light) 0%,#0a72c0 45%,var(--blue-dark) 100%)}
  .world-map{position:absolute;left:160px;top:45px;width:760px;height:460px;border-radius:45%;background:radial-gradient(ellipse at 50% 40%,rgba(90,170,235,.45),rgba(90,170,235,0) 70%)}

  .searcher-card{position:absolute;left:357px;top:118px;width:315px;height:257px;background:var(--white);box-shadow:0 2px 0 rgba(0,0,0,.15)}
  .searcher-title{height:49px;background:var(--card-head);border-bottom:1px solid #dcdcdc;color:var(--orange);font-size:24px;font-weight:400;text-align:center;line-height:49px}
  .searcher-field{position:absolute;left:24px;width:268px;height:45px;border:1px solid var(--field-border);box-shadow:inset 0 2px 2px rgba(0,0,0,.08);font-size:13px;color:var(--placeholder);padding-left:15px;line-height:45px}
  .field-company{top:74px}
  .field-location{top:130px}
  .search-button{position:absolute;left:24px;top:186px;width:268px;height:45px;background:var(--orange);color:var(--white);font-size:13px;font-weight:600;text-align:center;line-height:45px;border-radius:1px}

  .ad-slot{position:absolute;left:902px;top:42px;width:178px;height:423px;background:var(--white);display:flex;align-items:center;justify-content:center;text-align:center;color:#9a9a9a;font-size:28px;font-weight:300;line-height:24px}

  .footer-nav{position:absolute;top:591px;left:0;width:1200px;height:57px;background:var(--footer);font-size:14px;color:var(--footer-text);font-weight:400}
  .footer-nav span{position:absolute;top:19px;line-height:18px;white-space:nowrap}
  .copyright{position:absolute;top:669px;left:0;width:1200px;text-align:center;font-size:11px;color:#444}
</style>
</head>
<body>
  <header class="site-header">
    <div class="brand"><span class="brand-dot"></span><span class="brand-name">TALVEXO</span></div>
    <nav class="main-nav">
      <span class="is-active" style="left:472px">SEARCHER</span>
      <span style="left:547px">ADVISES</span>
      <span style="left:609px">JOBS</span>
      <span style="left:654px">SOLUTIONS</span>
      <span style="left:735px">ABOUT US</span>
    </nav>
    <div class="language-select"><span>LANGUAGE</span>
      <svg width="10" height="7" viewBox="0 0 10 7"><path d="M1 1l4 4 4-4" fill="none" stroke="#2b2b2b" stroke-width="2"/></svg>
    </div>
    <div class="login-button">LOGIN ACCOUNT</div>
  </header>

  <section class="hero">
    <div class="world-map" role="img" aria-label="Dotted world map illustration"></div>
    <div class="searcher-card">
      <h1 class="searcher-title">COMPANIES SEARCHER</h1>
      <div class="searcher-field field-company">COMPANY NAME / VAT NUMBER</div>
      <div class="searcher-field field-location">CITY / POST CODE / COUNTRY</div>
      <div class="search-button">SEARCH NOW</div>
    </div>
    <aside class="ad-slot">ADD<br>HERE</aside>
  </section>

  <footer>
    <nav class="footer-nav">
      <span style="left:237px">ABOUT US</span>
      <span style="left:342px">CONTACT US</span>
      <span style="left:462px">COMMUNITY</span>
      <span style="left:578px">PUBLICITY</span>
      <span style="left:682px">CONDITIONS</span>
      <span style="left:801px">POLITICS</span>
      <span style="left:898px">LANGUAGE</span>
    </nav>
    <p class="copyright">COPYRIGHT © 2015 TALVEXO. ALL RIGHTS RESERVED</p>
  </footer>
</body>
</html>
```